Bold, Modern, Clean "Vernatouchmassage.com" website

Why we stand out?
We are a male and female mobile massage team. Our names are Jonah and Tessa. 
Verna Touch is a Seattle based mobile massage service. Our massage is offered to the community with a goal of facilitating balance within each individual. We specialize in integrated Pain management, and sports/medical massage therapy. Every client's first assessment is attended by our male and female massage therapist team. Depending on the goals identified for an individual determines which therapist will be assigned to provide treatment, if not both.

Our passion...
Here at Verna Touch, we have a great passion for Postural Resoration and how it is integrated into an individual's Massage treatment. We pride ourselves in being natural facilitators of healing, which takes the ego of the therapist out of the client's healing process. We strive to deliver the best massage possible by including modalities such as Neuromuscular, Myofascial release, spontaneous muscle release, postural restoration, orthopedic, and medical massage.

Our education...

We are both Graduates of Alvenra, school of massage therapy. We have continuing education in medical massage, myofacial release, trigger point therapy, postural restoration, anatomy, and spontaneous muscle release. Tessa is also a Certified Yoga Instructor, which amplifies her experience with flexibility and strength as it pertains to each individual. Jonah's passion is Massage, stretching, and strength training to encourage postural restoration and realignment.

Our rates-

Our rates are $75/ 60 minutes, $95/ 90 minutes, and $120/ 120 minutes.

Education-
Both Tessa and I worked as behavioral health professionals that specialized in life skills mentoring for youth who had experienced different types of trauma. This led us both to want to help others in a different environment, where individuals can be empowered to take responsibility over their own healing. To us, massage is a type of manipulation physical therapy, that encourages healing on many levels.

Advice to any massage client-
The most important thing to 'us', as Licenced providers is to get you on to our table to show you our skills. But a good therapist never forgets that it's not about what we do for you, but what we can facilitate for you. Your health and healing has nothing to do with us. It is yours, not ours. Identify what your goals are with any Therapist, and know what the end looks like. Progress should be tangible, such as range of motion, and decreased pain.

5/5 stars Massage Therapy
Verified Review

Tessa and Jonah at Verna Touch are awesome! I recently had open heart surgery, and Tessa worked on me to increase my range of motion while helping with the pinched nerve from my arm being in the same position for so long during my surgery. My wife drives a lot for work, and Jonah has helped decrease her neck and lower back pain immensely. They are seriously the best therapists I have ever worked with. I would recommend them to anyone who needs anything from stress relief to a medical massage treatment. They are professional, up beat, easy going, and always on time. And, I love that they meet us where ever we like! We did a staycation recently, where they came to our hotel to give us relaxation massages. Although usually they come to our home, where we focus on pain related issues. We will continue to work with them for a long, long time.

Brisa K. on December 17, 2015

Target Market(s)

Mobile massage therapy clients

Industry/Entity Type

Massage Therapy

Coding

Coded - Design and coding required

Number of Pages Required

1 page

Font styles to use
Serif
Sans Serif

Requirements
Must have
• Please add or remove any information that would help the presentation of our website. Our logo is posted below, please include into the website.
• Please include a contact field that includes, vernatouchmassage@quillmail.test,
• (206) 555-0147
• We have also included our own stock photos, as well as a photo of Jonah and Tessa. Please include a cropped photo of both massage therapists.

```html
<!DOCTYPE html>
<html lang="en">
<head>
<meta charset="utf-8">
<title>Verna Touch mobile massage</title>
<link rel="stylesheet" href="https://fonts.googleapis.com/css2?family=Baumans&family=Montserrat:wght@400;500;600&family=Roboto:wght@400;500&display=swap">
<style>
:root{
  --blue:#0a27b2;
  --blue-deep:#0a2aa8;
  --teal:#18d6d6;
  --grey-band:#f2f2f2;
  --text:#333333;
  --muted:#777777;
  --white:#ffffff;
  --rule:#bdbdbd;
}
*{margin:0;padding:0;box-sizing:border-box}
html,body{width:1200px;height:2917px;overflow:hidden}
body{position:relative;font-family:"Roboto",sans-serif;color:var(--text);background:var(--white)}
.section{position:absolute;left:0;width:1200px}
.heading{position:absolute;left:0;width:1200px;text-align:center;font-family:"Baumans",sans-serif;font-size:42px;font-weight:400;color:var(--blue);line-height:1}
.heading-rule{position:absolute;left:450px;width:300px;height:1px;background:var(--rule)}
.copy{position:absolute;text-align:center;font-size:15px;line-height:29px;color:var(--text)}
.read-more{position:absolute;left:0;width:1200px;text-align:center;font-family:"Arial",sans-serif;font-weight:700;font-size:20px;color:var(--blue);text-decoration:underline}

/* hero */
.hero{top:0;height:677px;background:linear-gradient(180deg,#f4f1ee 0%,#ece6df 55%,#d9cbb8 100%)}
.hero-photo{position:absolute;inset:0;background:linear-gradient(90deg,#efe9e3 0%,#f7f4f1 50%,#eae3da 100%)}
.nav{position:absolute;top:0;left:0;width:1200px;height:58px;background:linear-gradient(180deg,#7b7b7b,#4a4a4a)}
.nav-list{position:absolute;left:228px;top:0;display:flex;list-style:none;height:58px}
.nav-list li{font-family:"Montserrat",sans-serif;font-weight:600;font-size:14px;color:var(--white);line-height:58px;padding:0 28px}
.nav-list li.is-active{background:var(--teal)}
.brand{position:absolute;left:498px;top:197px;width:202px;height:202px;border-radius:50%;background:var(--blue);display:flex;align-items:center;justify-content:center;text-align:center}
.brand-name{font-family:"Montserrat",sans-serif;font-weight:600;font-size:30px;line-height:34px;color:var(--white)}
.dots{position:absolute;top:634px;left:570px;display:flex;gap:10px}
.dot{width:11px;height:11px;border-radius:50%;background:#111}
.dot.is-current{background:transparent;border:2px solid #111}

/* who */
.who{top:677px;height:363px;background:var(--grey-band)}

/* services */
.services{top:1040px;height:532px;background:var(--white)}
.services-lead{position:absolute;top:141px;left:0;width:1200px;text-align:center;font-size:15px;color:var(--text)}
.service{position:absolute;top:200px;width:260px;text-align:center}
.service-badge{width:172px;height:172px;margin:0 auto;border-radius:50%;background:linear-gradient(180deg,#0b36c4 0%,#0a6fd6 60%,#16d4dc 100%);display:flex;align-items:center;justify-content:center}
.service-badge span{width:134px;height:134px;border-radius:50%;background:linear-gradient(180deg,#0b2fb6,#0d8fe0);border:2px solid rgba(255,255,255,.35)}
.service-title{margin-top:40px;font-family:"Montserrat",sans-serif;font-weight:500;font-size:17px;color:#111}
.service-text{margin-top:12px;font-size:14px;line-height:23px;color:var(--muted)}
.service-divider{position:absolute;top:210px;width:1px;height:108px;background:#d5d5d5}

/* education */
.education{top:1572px;height:344px;background:var(--grey-band)}

/* rates */
.rates{top:1916px;height:364px;background:linear-gradient(100deg,#2a1b10 0%,#4a3525 40%,#3a2a1d 65%,#1c130c 100%)}
.rates .heading{color:var(--white)}
.rates .heading-rule{background:rgba(255,255,255,.5)}
.rate{position:absolute;top:167px;width:136px;height:136px;border-radius:50%;border:3px solid var(--white);display:flex;align-items:center;justify-content:center;text-align:center;font-family:"Montserrat",sans-serif;font-weight:500;font-size:18px;line-height:23px;color:var(--white)}
.rate::after{content:"";position:absolute;inset:5px;border-radius:50%;border:2px solid transparent;border-left-color:var(--teal);border-bottom-color:var(--teal)}

/* testimonials */
.testimonials{top:2280px;height:346px;background:var(--white)}
.review-date{position:absolute;left:119px;top:138px;width:132px;height:132px;border-radius:50%;border:3px solid var(--blue);display:flex;align-items:center;justify-content:center;text-align:center;font-family:"Montserrat",sans-serif;font-size:15px;line-height:22px;color:#111}
.review-date::after{content:"";position:absolute;inset:5px;border-radius:50%;border:2px solid transparent;border-left-color:var(--teal);border-bottom-color:var(--teal)}
.review-text{position:absolute;left:282px;top:155px;width:800px;font-size:15px;line-height:25px;color:var(--text)}
.review-author{position:absolute;left:282px;top:270px;font-family:"Montserrat",sans-serif;font-weight:500;font-size:16px;color:#111}

/* footer */
.footer{top:2626px;height:291px;background:var(--blue-deep);color:var(--white)}
.to-top{position:absolute;left:575px;top:-25px;width:50px;height:50px;border-radius:50%;background:var(--white);border:2px solid var(--blue-deep);display:flex;align-items:center;justify-content:center}
.contact-phone{position:absolute;right:713px;top:80px;font-size:15px}
.contact-mail{position:absolute;left:710px;top:80px;font-size:15px}
.contact-icon{position:absolute;top:50px;width:82px;height:82px;border-radius:50%;border:2px solid var(--white);display:flex;align-items:center;justify-content:center}
.contact-icon::after{content:"";position:absolute;inset:5px;border-radius:50%;border:1px solid rgba(255,255,255,.6)}
.footer-nav{position:absolute;top:165px;left:0;width:1200px;display:flex;justify-content:center;list-style:none;font-family:"Montserrat",sans-serif;font-weight:600;font-size:14px}
.footer-nav li{padding:0 30px;position:relative}
.footer-nav li+li::before{content:"|";position:absolute;left:-3px}
.footer-rule{position:absolute;top:216px;left:78px;width:1044px;height:1px;background:#2f6fe0}
.copyright{position:absolute;top:244px;left:0;width:1200px;text-align:center;font-family:"Montserrat",sans-serif;font-size:14px;color:#0a0a2a}
</style>
</head>
<body>

<header class="section hero">
  <div class="hero-photo" role="img" aria-label="Photo of two massage therapists treating a woman and a man lying on massage tables"></div>
  <nav class="nav">
    <ul class="nav-list">
      <li class="is-active">Home</li><li>About us</li><li>Our Passion</li><li>Education</li><li>Testimonial</li><li>Contact Us</li>
    </ul>
  </nav>
  <div class="brand"><span class="brand-name">Verna<br>Touch</span></div>
  <div class="dots"><span class="dot"></span><span class="dot is-current"></span><span class="dot"></span></div>
</header>

<section class="section who">
  <h2 class="heading" style="top:62px">Who We Are</h2>
  <div class="heading-rule" style="top:120px"></div>
  <p class="copy" style="top:140px;left:160px;width:880px">We are a male and female mobile massage team. Our names are Jonah and Tessa.<br>Verna Touch is a Seattle based mobile massage service. Our massage is offered to the community with a goal of facilitating balance within each individual. We specialize in integrated Pain management, and sports/medical massage therapy. Every client's first assessment is attended by our male and female massage therapist team.</p>
  <a class="read-more" style="top:281px">READ MORE</a>
</section>

<section class="section services">
  <h2 class="heading" style="top:56px">What We Do</h2>
  <div class="heading-rule" style="top:114px"></div>
  <p class="services-lead">We strive to deliver the best massage possible by including modalities</p>
  <div class="service" style="left:74px"><div class="service-badge" role="img" aria-label="Neuromuscular icon"><span></span></div><h3 class="service-title">Neuromuscular</h3><p class="service-text">Lorem ipsum dolor sit amet,<br>consectetur adipiscing elit,send.</p></div>
  <div class="service-divider" style="left:337px"></div>
  <div class="service" style="left:341px"><div class="service-badge" role="img" aria-label="Spontaneous muscle release icon"><span></span></div><h3 class="service-title">Spontaneous Muscle Release</h3><p class="service-text">Lorem ipsum dolor sit amet,<br>consectetur adipiscing elit,send.</p></div>
  <div class="service-divider" style="left:603px"></div>
  <div class="service" style="left:605px"><div class="service-badge" role="img" aria-label="Postural restoration icon"><span></span></div><h3 class="service-title">postural restoration</h3><p class="service-text">Lorem ipsum dolor sit amet,<br>consectetur adipiscing elit,send.</p></div>
  <div class="service-divider" style="left:866px"></div>
  <div class="service" style="left:870px"><div class="service-badge" role="img" aria-label="Medical massage icon"><span></span></div><h3 class="service-title">Medical Massage</h3><p class="service-text">Lorem ipsum dolor sit amet,<br>consectetur adipiscing elit,send.</p></div>
</section>

<section class="section education">
  <h2 class="heading" style="top:60px">Our Education</h2>
  <div class="heading-rule" style="top:120px"></div>
  <p class="copy" style="top:146px;left:150px;width:900px">We are both Graduates of Alvenra, school of massage therapy. We have continuing education in medical massage, myofacial release, trigger point therapy, postural restoration, anatomy, and spontaneous muscle release. Tessa is also a Certified Yoga Instructor, which amplifies her experience with flexibility and strength as it pertains to each individual</p>
  <a class="read-more" style="top:266px">READ MORE</a>
</section>

<section class="section rates" role="img" aria-label="Dimmed photo of a therapist massaging a client's shoulders">
  <h2 class="heading" style="top:55px">Our Rate</h2>
  <div class="heading-rule" style="top:117px"></div>
  <div class="rate" style="left:329px">$ 75 / 60<br>Minutes</div>
  <div class="rate" style="left:537px">$ 95 / 90<br>Minutes</div>
  <div class="rate" style="left:737px">$ 120 / 120<br>Minutes</div>
</section>

<section class="section testimonials">
  <h2 class="heading" style="top:58px">Testimonials</h2>
  <div class="heading-rule" style="top:116px"></div>
  <div class="review-date">December 17,<br>2015</div>
  <p class="review-text">Tessa and Jonah at Verna Touch are awesome! I recently had open heart surgery, and Tessa worked on me to increase my range of motion while helping with the pinched nerve from my arm being in the same position for so long during my surgery. My wife drives a lot for work, and Jonah has helped decrease her neck and lower back pain immensely. They are seriously the best therapists I have ever worked with</p>
  <p class="review-author">- Brisa K.</p>
</section>

<footer class="section footer">
  <div class="to-top">
    <svg width="18" height="18" viewBox="0 0 18 18" aria-hidden="true"><path d="M4 9 L9 4 L14 9 M4 14 L9 9 L14 14" fill="none" stroke="#0a0a2a" stroke-width="2.5"/></svg>
  </div>
  <span class="contact-phone">(206) 555-0147</span>
  <div class="contact-icon" style="left:509px">
    <svg width="22" height="22" viewBox="0 0 24 24" aria-hidden="true"><path fill="#fff" d="M6.6 10.8a15.2 15.2 0 0 0 6.6 6.6l2.2-2.2c.3-.3.7-.4 1-.2 1.1.4 2.3.6 3.6.6.6 0 1 .4 1 1V20c0 .6-.4 1-1 1A17 17 0 0 1 3 4c0-.6.4-1 1-1h3.5c.6 0 1 .4 1 1 0 1.3.2 2.5.6 3.6.1.3 0 .7-.2 1z"/></svg>
  </div>
  <div class="contact-icon" style="left:609px">
    <svg width="22" height="18" viewBox="0 0 22 18" aria-hidden="true"><rect x="1" y="2" width="20" height="14" rx="2" fill="#fff"/><path d="M2 3 L11 10 L20 3" fill="none" stroke="#0a2aa8" stroke-width="1.8"/></svg>
  </div>
  <span class="contact-mail">vernatouchmassage@quillmail.test</span>
  <ul class="footer-nav">
    <li>Home</li><li>About us</li><li>Our Passion</li><li>Education</li><li>Testimonial</li><li>Contact Us</li>
  </ul>
  <div class="footer-rule"></div>
  <p class="copyright">© Verna Touch mobile massage . 2015. All rights reserved.</p>
</footer>

</body>
</html>
```